Plofzon car advertisement

de website moet uit minimaal 3 pagina's bestaan. 1 pagina als een landingspagina. 1 pagina voor consumenten die hun auto willen laten beplakken met bedrijfsreclame en 1 pagina voor bedrijven / consumenten die hun bedrijfsreclame op een consumentenauto wilt plaatsen.

de website moet echt een happy website zijn. consumenten kunnen geld verdienen met reclame op hun auto te laten zetten en bedrijven kunnen voor een relatief goedkoop bedrag hun bedrijfsreclame op een auto laten zetten. die auto rijdt dan rond en veel mensen zien de reclame.

beide pagina's moeten dus een glimlach opleveren.

het doel van de startpagina is dat je door kunt gaan naar de consumenten en de bedrijfspagina.

gebruik leuke, vrolijke kleuren en vormen en zorg dat de mensen een glimlach krijgen als ze naar de website kijken.

doelgroep is consumenten die een auto rijden en geld willen verdienen met hun auto en de zakelijke ondernemer die voor een goedkoop bedrag zijn bedrijfsreclame met een full carwrap kan laten zien aan de buitenwereld.

doordat consumenten zich bij ons aanmelden hebben wij een database met auto's en weten we hoeveel deze auto's rijden en in welke regio's ze rijden en wat voor auto ze rijden. allemaal hele belangrijke informatie voor een ondernemer die reclame wilt maken op ene specifieke auto type en in een bepaalde regio.

-

website should consist of at least 3 pages. 1 landing page, 1 customer page and 1 business page. landing page let's the visitor choose wether he / she is a customer with a car and wants to allow his car to be fully carwrapped or he / she is a business owner who wants to place his advertisement on a car.

website should be a really happy joyfull website and bring a smile to the visitor. beause the customer can earn money (200 euro / month nett) by allowing advertisements on his car (full car wrap) and the business owner because for a low price he can advertise.

when customers that owns a car register themselves with our website we build a database with cars in specific locations. a business owner wants to advertise his product into a specific region. this is very valuable information.

agreement is 1 year for a customer to have advertisements on his car and for a business to advertise. after that year, the advertisements are safely removed from the car and new advertisement agreements can be made. a business can place advertisements (full carwrap) already for 795 euro's., Details for my new Web Design Project will be added soon. , de website moet uit minimaal 3 pagina's bestaan. 1 pagina als een landingspagina. 1 pagina voor consumenten die hun auto willen laten beplakken met bedrijfsreclame en 1 pagina voor bedrijven / consumenten die hun bedrijfsreclame op een consumentenauto wilt plaatsen.

Target Market(s)

customers who has a car
businesses who want to advertise their business / product on a car

Industry/Entity Type

Business

Requirements
Must have
• website should be playfull, colorfull and a joy to look at and work with. altough functoinality is very limited visitors need to be intrigued to proceed to contact plofzon.
Nice to have
• nice graphics, moving images, a "living" website (not so static)

```html
<!DOCTYPE html>
<html lang="en">
<head>
<meta charset="utf-8">
<title>Plofzon – Register Your Car</title>
<link href="https://fonts.googleapis.com/css2?family=Roboto:ital,wght@0,300;0,400;0,500;0,700;1,300&display=swap" rel="stylesheet">
<style>
  :root {
    --orange: #f7941d;
    --ink: #555b5e;
    --ink-dark: #3d4245;
    --heading: #4a5054;
    --line: #d8d8d8;
    --white: #ffffff;
    --nav-bg: rgba(238, 240, 242, 0.93);
    --footer-bg: #14191c;
    --footer-text: #e6e6e6;
  }
  * { box-sizing: border-box; margin: 0; padding: 0; }
  html, body { width: 1185px; height: 1200px; overflow: hidden; }
  body {
    position: relative;
    font-family: "Roboto", Arial, sans-serif;
    color: var(--ink);
    background: #2b3a4a;
  }
  .city-backdrop {
    position: absolute; inset: 0;
    background:
      radial-gradient(ellipse 260px 520px at 60px 380px, rgba(240,220,170,0.55), transparent 70%),
      radial-gradient(ellipse 200px 420px at 1120px 600px, rgba(140,180,220,0.45), transparent 70%),
      linear-gradient(180deg, #4d5f6e 0%, #2d3a47 40%, #3a4c5c 70%, #243240 100%);
  }
  .abs { position: absolute; }

  /* top controls */
  .slider-controls { left: 1073px; top: 9px; width: 100px; height: 20px; }

  /* header */
  .brand {
    left: 143px; top: 34px;
    font-size: 34px; font-weight: 700; color: var(--orange);
    letter-spacing: -0.5px; line-height: 38px;
  }
  .header-rule { left: 142.5px; top: 73px; width: 900px; height: 8.5px;
    background: linear-gradient(180deg, #2a3034, #454c51); }
  .header-tools { left: 898px; top: 30px; width: 144.5px; height: 43px;
    background: rgba(30,35,38,0.9); display: flex; align-items: center; padding-left: 20px; gap: 7px; }
  .lang { width: 14px; height: 10px; }
  .lang.nl { background: linear-gradient(180deg, #c8232c 33%, #fff 33% 66%, #21468b 66%); }
  .lang.en { background: #2b3f8a; }
  .tools-sep { width: 1px; height: 18px; background: #666; margin: 0 4px; }
  .social { width: 13px; height: 13px; border-radius: 50%; background: #e9e9e9; }

  /* nav */
  .main-nav { left: 142.5px; top: 81.5px; width: 590.5px; height: 75px; background: var(--nav-bg);
    display: flex; align-items: stretch; font-size: 12.5px; font-weight: 300; }
  .main-nav a { color: #6f7579; text-decoration: none; display: flex; align-items: center; padding: 0 14px; }
  .main-nav a.active { background: var(--orange); color: var(--white); }
  .testimonial { left: 733px; top: 81.5px; width: 309.5px; height: 75px; background: var(--white);
    padding: 13px 10px 0 10px; border-top: 4px solid #eee; }
  .testimonial .label { font-size: 9.5px; color: var(--orange); line-height: 12px; }
  .testimonial q { display: block; font-size: 11px; font-style: italic; font-weight: 300; color: #666; line-height: 11.5px; margin-top: 2px; }
  .testimonial .author { font-size: 9.5px; color: #333; margin-top: 3px; }

  /* content */
  .page { left: 142.5px; top: 156.5px; width: 900px; height: 864.5px; background: var(--white); }
  .section-title { font-size: 24px; font-weight: 300; color: var(--heading); line-height: 28px; }
  .hatch { height: 5px;
    background: repeating-linear-gradient(135deg, #d5d5d5 0 1px, transparent 1px 3px); }
  .car-visual { left: 246px; top: 248px; width: 392px; height: 174px; border-radius: 60px 90px 20px 20px;
    background: linear-gradient(180deg, #3a4d6e 0%, #8c1f24 45%, #7a1a1d 75%, #2e2e30 100%); }
  .intro { left: 170.5px; top: 429px; width: 556px; font-size: 11.8px; font-weight: 300; line-height: 17px; color: var(--ink); }
  .form-title { font-size: 21px; }
  .form-hint { left: 170.5px; top: 584px; font-size: 12.5px; font-weight: 300; }
  .form-divider { left: 355px; top: 579px; width: 26px; height: 394px; }
  .field-label { font-size: 12px; font-weight: 500; color: var(--ink-dark); letter-spacing: 0.3px; }
  .text-input { width: 304px; height: 21px; border: 1px solid #cfcfcf; background: var(--white); }
  .requirements { left: 393px; top: 835px; width: 304px; height: 52px; border: 1px solid #cfcfcf; padding: 14px 0 0 15px; }
  .requirements h3 { font-size: 15px; font-weight: 300; color: #666; line-height: 18px; }
  .requirements p { font-size: 8px; color: #555; letter-spacing: 0.4px; margin-top: 1px; padding-left: 3px; }
  .btn { background: var(--orange); color: var(--white); font-size: 12.5px; font-weight: 300;
    display: flex; align-items: center; justify-content: center; }

  /* sidebar */
  .login-box { left: 780px; top: 247.5px; width: 234px; height: 211px; border: 2px dotted #d3d3d3; }
  .forgot { font-size: 11px; color: var(--orange); }
  .video-frame { left: 780px; top: 545px; width: 234px; height: 134px;
    background: linear-gradient(180deg, #222 0%, #6b6a4e 40%, #4c5138 75%, #1c1c1c 100%); }
  .faq-item { left: 786px; width: 228px; font-size: 10.3px; line-height: 15px; font-weight: 300; color: #4a4a4a; }
  .faq-item h4 { font-size: 11.5px; font-weight: 300; color: #8a8f92; padding-left: 12px; position: relative; line-height: 14px; margin-bottom: 1px; }
  .faq-item h4::before { content: ""; position: absolute; left: 0; top: 4px; border: 3.5px solid transparent; border-left-color: #bbb; }
  .faq-item p { padding-left: 11px; }

  /* footer */
  .site-footer { left: 142.5px; top: 1021px; width: 900px; height: 162px;
    background: linear-gradient(180deg, #22292d 0%, var(--footer-bg) 60%, #101416 100%); }
  .footer-col { top: 1043px; width: 262.5px; color: var(--footer-text); font-size: 11.5px; line-height: 16px; }
  .footer-col h2 { font-size: 19.5px; font-weight: 400; color: var(--white); line-height: 24px;
    padding-bottom: 3px; border-bottom: 1px solid #5a6064; margin-bottom: 8px; }
  .contact-line { display: flex; align-items: center; gap: 5px; }
  .news-input { left: 761px; top: 1105px; width: 131px; height: 23px; background: #ececec; }
  .news-btn { left: 891.5px; top: 1105px; width: 65.5px; height: 23px; font-size: 11.5px; font-weight: 400; }
  .copyright { left: 161px; top: 1154px; font-size: 8px; color: var(--footer-text); }
</style>
</head>
<body>
  <div class="city-backdrop" role="img" aria-label="Blurred night city street with streaking traffic lights"></div>

  <svg class="abs slider-controls" viewBox="0 0 100 20" aria-hidden="true">
    <g fill="none" stroke="#8a9299" stroke-width="2">
      <path d="M2 7V2h5M15 2h5v5M20 13v5h-5M7 18H2v-5"/>
      <path d="M63 3l-7 7 7 7M83 3l7 7-7 7"/>
    </g>
    <path d="M32 1v18l14-9z" fill="#8a9299"/>
  </svg>

  <header>
    <div class="abs brand">Plofzon</div>
    <div class="abs header-rule"></div>
    <div class="abs header-tools">
      <span class="lang nl"></span><span class="lang en"></span>
      <span class="tools-sep"></span>
      <span class="social"></span><span class="social"></span><span class="social"></span>
    </div>
    <nav class="abs main-nav">
      <a href="#">Home</a>
      <a href="#" class="active">Car Holders</a>
      <a href="#">Business Holders</a>
      <a href="#">Advertisers</a>
      <a href="#">Our Works</a>
      <a href="#">Contact</a>
    </nav>
    <aside class="abs testimonial">
      <div class="label">Testimonials</div>
      <q>Duis in jus letalis pagus patria verto. Duis eligo facilisis ideo nostrud paratus ulciscor.</q>
      <div class="author">John Smith</div>
    </aside>
  </header>

  <main class="abs page"></main>

  <h1 class="abs section-title" style="left:170.5px; top:197px;">Register Your Car</h1>
  <div class="abs hatch" style="left:170.5px; top:228px; width:553px;"></div>
  <div class="abs car-visual" role="img" aria-label="Compact hatchback in a full red advertising car wrap"></div>
  <p class="abs intro">Accumsan diam imputo. Amet autem conventio facilisi hos ideo imputo inhibeo similis ut. Autem enim lucidus minim quidem ut. Exputo inhibeo iriure jumentum magna mauris nobis pneum refero vel. Et fere genitus haero inhibeo nunc similis te. Amet esse eu illum importunus melior os refero suscipit virtus. Duis fere haero huic humo imputo pneum rusticus scisco. Conventio premo tamen.</p>

  <h2 class="abs section-title form-title" style="left:170.5px; top:535px;">Registration Form</h2>
  <div class="abs form-hint">Please complete this form:</div>
  <svg class="abs form-divider" viewBox="0 0 26 394" aria-hidden="true">
    <path d="M4 0v15l18 21-18 21v337" fill="none" stroke="#dcdcdc" stroke-width="1"/>
  </svg>

  <label class="abs field-label" style="left:393px; top:585px;">Your name</label>
  <div class="abs text-input" style="left:393px; top:602px;"></div>
  <label class="abs field-label" style="left:393px; top:636px;">Username</label>
  <div class="abs text-input" style="left:393px; top:652.5px;"></div>
  <label class="abs field-label" style="left:393px; top:687px;">Car registration number</label>
  <div class="abs text-input" style="left:393px; top:703px;"></div>
  <label class="abs field-label" style="left:393px; top:737px;">Choose a password</label>
  <div class="abs text-input" style="left:393px; top:754px;"></div>
  <label class="abs field-label" style="left:393px; top:787px;">Password repeat</label>
  <div class="abs text-input" style="left:393px; top:804px;"></div>
  <div class="abs requirements">
    <h3>Requirements</h3>
    <p>All the fields are mandatory</p>
  </div>
  <div class="abs btn" style="left:393px; top:918px; width:64.5px; height:37px;">Submit</div>

  <h2 class="abs section-title" style="left:780px; top:198px;">Customer login</h2>
  <div class="abs hatch" style="left:780px; top:228px; width:234px;"></div>
  <div class="abs login-box"></div>
  <label class="abs field-label" style="left:800.5px; top:271px;">Username</label>
  <div class="abs text-input" style="left:800.5px; top:288px; width:193.5px;"></div>
  <label class="abs field-label" style="left:800.5px; top:320px;">Password</label>
  <div class="abs text-input" style="left:800.5px; top:335.5px; width:193.5px;"></div>
  <a class="abs forgot" style="left:800.5px; top:367px;">Forget your password?</a>
  <div class="abs btn" style="left:800.5px; top:392px; width:64.5px; height:37px;">Submit</div>

  <h2 class="abs section-title" style="left:780px; top:494px;">Embed video</h2>
  <div class="abs hatch" style="left:780px; top:526px; width:234px;"></div>
  <div class="abs video-frame" role="img" aria-label="Embedded video player showing a still from a travel video"></div>

  <h2 class="abs section-title" style="left:780px; top:717px;">FAQ</h2>
  <div class="abs hatch" style="left:780px; top:750px; width:234px;"></div>
  <div class="abs faq-item" style="top:768px;">
    <h4>Duis Interdico Te</h4>
    <p>Duis in jus letalis pagus patria verto. Duis eligo facilisis ideo nostrud paratus ulciscor.</p>
  </div>
  <div class="abs faq-item" style="top:818px;">
    <h4>Caecus Exputo Iustum Quis</h4>
    <p>Ludus nostrud os pala tum venio. Diam dolore eros hendrerit inhibeo lobortis metuo quibus quis tego.</p>
  </div>
  <div class="abs faq-item" style="top:881px;">
    <h4>Et Feugiat Quadrum</h4>
    <p>Dolor gilvus neque occuro scisco suscipit vereor voco volutpat. Decet gemino ludus premo quidne refero utrum.</p>
  </div>

  <footer class="abs site-footer"></footer>
  <section class="abs footer-col" style="left:161px;">
    <h2>About us</h2>
    <p>Duis in jus letalis pagus patria verto. Duis eligo facilisis ideo nostrud paratus ulciscor. Duis in jus letalis pagus patria verto.</p>
  </section>
  <section class="abs footer-col" style="left:461px;">
    <h2>Contact us</h2>
    <p>Street Address</p>
    <p>Locality, Region, Netherlands</p>
    <p class="contact-line" style="margin-top:10px;">
      <svg width="10" height="13" viewBox="0 0 10 13" aria-hidden="true"><rect x="1.5" y="0.5" width="7" height="12" rx="1" fill="none" stroke="#fff"/><rect x="3" y="2" width="4" height="7" fill="#fff"/></svg>+31-000-00000
    </p>
    <p class="contact-line">
      <svg width="12" height="9" viewBox="0 0 12 9" aria-hidden="true"><rect width="12" height="9" fill="#fff"/><path d="M0 0l6 5 6-5" fill="none" stroke="#14191c"/></svg>contact@plofzon.nl
    </p>
  </section>
  <section class="abs footer-col" style="left:761px;">
    <h2>Newsletter</h2>
    <p>Stay informed on our latest news!</p>
  </section>
  <div class="abs news-input"></div>
  <div class="abs btn news-btn">Subscribe</div>
  <div class="abs copyright">© 2013 Plofzon. All rights reserved</div>
</body>
</html>
```